CPA, Management and IT Consulting Redesign Existing Website

We currently have a website that is outdated (www.kelvorant.com). We need a good website developer that can redesign our website. To make this easier I have chosen a few websites that we like the layout or template. Use our exiting website content for this project. Our new logo is attached below. Based on who wins this we will upgrade to a coded website and a content management system (CMS) so we can make changes to the text ourselves in the future.

http://www.marbeckhollis.com/
http://www.quorvelmanagement.com/

Target Market(s)

Government Clients

Industry/Entity Type

Management Consulting

Number of Pages Required

5+ page

Font styles to use
Serif

Requirements
Must have
• Please the following website templates as a guide.
• http://www.marbeckhollis.com/
• http://www.quorvelmanagement.com/
Nice to have
Should not have

```html
<!DOCTYPE html>
<html lang="en">
<head>
<meta charset="utf-8">
<title>Brennick Enterprises, LLC</title>
<link rel="stylesheet" href="https://fonts.googleapis.com/css2?family=Roboto:wght@300;400;500;700&display=swap">
<style>
:root{
  --orange:#f5962c;
  --ink:#222222;
  --text:#555555;
  --muted:#6d6d6d;
  --light:#f2f2f2;
  --white:#ffffff;
  --dark:#1d1d1d;
  --footer:#1a1a1a;
  --footer-text:#a9a9a9;
  --rule:#dddddd;
}
*{box-sizing:border-box;margin:0;padding:0}
html,body{width:1200px;height:2579px;overflow:hidden}
body{position:relative;font-family:'Roboto',sans-serif;color:var(--text);background:var(--white)}
a{color:inherit;text-decoration:none}

/* Header */
.site-header{position:absolute;left:0;top:0;width:1200px;height:110px;background:var(--white)}
.brand{position:absolute;left:74px;top:30px;display:flex;align-items:center;gap:12px}
.brand-mark{width:40px;height:40px;background:var(--orange)}
.brand-name{font-weight:700;font-size:24px;color:var(--ink);line-height:1;letter-spacing:.3px}
.social{position:absolute;top:18px;right:74px;display:flex;gap:10px}
.social span{width:36px;height:36px;border-radius:50%;background:var(--orange);display:block}
.main-nav{position:absolute;right:74px;top:76px;display:flex;gap:36px;font-size:13px;font-weight:500;color:var(--ink)}
.main-nav a{position:relative;padding:0 8px;height:34px;display:block}
.main-nav a.active{color:var(--orange)}
.main-nav a.active::after{content:"";position:absolute;left:0;right:0;bottom:0;height:3px;background:var(--orange)}

/* Hero */
.hero{position:absolute;left:0;top:110px;width:1200px;height:602px;
  background:radial-gradient(ellipse at 55% 40%,#7a8384 0%,#5d6566 45%,#3d4344 100%)}
.hero-photo{position:absolute;inset:0}
.hero-content{position:absolute;left:0;right:0;top:200px;text-align:center;color:var(--white)}
.hero-title{font-size:46px;font-weight:700;letter-spacing:.5px}
.hero-text{width:660px;margin:20px auto 0;font-size:16.5px;line-height:24px;font-weight:400}
.btn{display:inline-block;background:var(--orange);color:var(--white);font-size:14px;font-weight:500;text-transform:uppercase;letter-spacing:.3px}
.hero .btn{margin-top:28px;width:143px;height:44px;line-height:44px}
.hero-arrow{position:absolute;top:263px;width:38px;height:54px;background:rgba(20,20,20,.75)}
.hero-arrow.prev{left:0}.hero-arrow.next{right:0}
.hero-arrow svg{position:absolute;left:12px;top:19px}
.hero-dots{position:absolute;left:0;right:0;top:570px;display:flex;justify-content:center;gap:8px}
.hero-dots span{width:10px;height:10px;border-radius:50%;border:1.5px solid var(--white)}
.hero-dots span.on{background:var(--white)}

/* Welcome */
.welcome{position:absolute;left:0;top:712px;width:1200px;height:361px;text-align:center}
.section-title{font-size:26px;font-weight:500;color:var(--ink);letter-spacing:.3px}
.welcome .section-title{margin-top:82px}
.welcome-text{width:960px;margin:30px auto 0;font-size:13px;line-height:22.5px;color:var(--muted)}
.welcome .btn{margin-top:26px;width:178px;height:40px;line-height:40px;font-size:13px}

/* Services */
.services{position:absolute;left:0;top:1073px;width:1200px;height:432px;background:var(--light);text-align:center}
.services .section-title{margin-top:64px}
.title-rule{width:60px;height:3px;background:var(--orange);margin:14px auto 0}
.service-list{position:absolute;left:60px;top:140px;width:1080px;display:flex}
.service{width:270px}
.service svg{display:block;margin:0 auto}
.service h3{margin-top:24px;font-size:19px;font-weight:400;color:var(--ink);line-height:23px;height:46px}
.service p{margin-top:10px;font-size:13px;line-height:19px;color:var(--muted)}

/* Industries */
.industries{position:absolute;left:0;top:1505px;width:1200px;height:533px;
  background:linear-gradient(135deg,#2a2b2c 0%,#161616 55%,#222324 100%);text-align:center;color:var(--white)}
.industries .section-title{color:var(--white);margin-top:70px}
.industries-intro{width:860px;margin:30px auto 0;font-size:15.5px;line-height:23px;color:#9a9a9a}
.industry-list{position:absolute;left:74px;top:221px;display:flex;gap:28px}
.industry{width:243px}
.industry-photo{height:194px}
.industry h3{margin-top:22px;font-size:16.5px;font-weight:400}
.photo-capitol{background:linear-gradient(180deg,#5c8ed2 0%,#a9c6e8 45%,#c9c0a8 70%,#5b7d3c 100%)}
.photo-columns{background:linear-gradient(90deg,#8a7f74 0%,#e8e2da 30%,#a59a8e 55%,#efe9e1 80%,#7c7167 100%)}
.photo-finance{background:linear-gradient(160deg,#3d6fa3 0%,#8db6dc 50%,#dfe9f2 100%)}
.photo-nonprofit{background:linear-gradient(180deg,#c9ced4 0%,#e9ebee 50%,#b9bec4 100%)}

/* Partner badges */
.partners{position:absolute;left:0;top:2038px;width:1200px;height:172px;background:var(--white)}
.badge-list{position:absolute;left:74px;top:44px;display:flex;gap:26px}
.badge{width:154px;height:88px;border:1px solid var(--rule);position:relative}
.badge span{position:absolute;left:32px;right:32px;top:30px;height:28px;background:#d9dde3}

/* Footer */
.site-footer{position:absolute;left:0;top:2210px;width:1200px;height:369px;background:var(--footer)}
.footer-cols{position:absolute;left:74px;top:52px;display:flex}
.footer-col{width:270px}
.footer-col h4{font-size:15.5px;font-weight:500;color:var(--orange);text-transform:uppercase;margin-bottom:16px}
.footer-col li{list-style:none;font-size:12.5px;line-height:27.5px;color:var(--footer-text);padding-left:18px;position:relative}
.footer-col li::before{content:"»";position:absolute;left:0;color:var(--orange)}
.contact li::before{content:none}
.contact li{padding-left:26px;line-height:19px;margin-bottom:10px}
.contact li svg{position:absolute;left:0;top:3px}
.footer-bottom{position:absolute;left:74px;right:74px;top:268px;border-top:1px solid #2e2e2e;padding-top:30px;text-align:center;font-size:12.5px;line-height:24px;color:var(--footer-text)}
</style>
</head>
<body>

<header class="site-header">
  <div class="brand"><span class="brand-mark"></span><span class="brand-name">BRENNICK ENTERPRISES, LLC</span></div>
  <div class="social"><span></span><span></span></div>
  <nav class="main-nav">
    <a class="active" href="#">HOME</a>
    <a href="#">ABOUT US</a>
    <a href="#">SERVICES</a>
    <a href="#">INDUSTRIES</a>
    <a href="#">CONTACT US</a>
  </nav>
</header>

<section class="hero">
  <div class="hero-photo" role="img" aria-label="Photo of a Newton's cradle with polished steel balls on a grey background"></div>
  <a class="hero-arrow prev" href="#"><svg width="14" height="16" viewBox="0 0 14 16"><path d="M10 1 3 8l7 7" fill="none" stroke="#fff" stroke-width="2"/></svg></a>
  <a class="hero-arrow next" href="#"><svg width="14" height="16" viewBox="0 0 14 16"><path d="M4 1l7 7-7 7" fill="none" stroke="#fff" stroke-width="2"/></svg></a>
  <div class="hero-content">
    <h1 class="hero-title">FINANCIAL AUDIT</h1>
    <p class="hero-text">Sed ut perspiciatis unde omnis iste natus error sit voluptatem accusantium doloremque laudantium, totam rem aperiam, eaque ipsa quae ab inventore.</p>
    <a class="btn" href="#">Learn More</a>
  </div>
  <div class="hero-dots"><span class="on"></span><span></span><span></span></div>
</section>

<section class="welcome">
  <h2 class="section-title">WELCOME TO BRENNICK</h2>
  <p class="welcome-text">Brennick Enterprises, LLC and Ashdale &amp; Mercer, LLC is a network of certified public accounting and management consulting firms with seasoned professionals and an excellent reputation for serving a diverse client base including federal agencies, state and local government, non-profit organizations, small and medium-sized business entities, professional associations and individuals. We are committed to professional excellence across all service areas including Audit and Assurance, Accounting, Tax, Management Consulting, and Information Technology.</p>
  <a class="btn" href="#">Find Out More &#10148;</a>
</section>

<section class="services">
  <h2 class="section-title">SERVICES AND SOLUTIONS</h2>
  <div class="title-rule"></div>
  <div class="service-list">
    <div class="service">
      <svg width="90" height="90" viewBox="0 0 90 90" fill="none" stroke="#f5962c" stroke-width="5">
        <rect x="4" y="4" width="82" height="82" rx="12"/>
        <rect x="14" y="14" width="28" height="28" rx="4" fill="#f5962c" stroke="none"/>
        <rect x="48" y="14" width="28" height="28" rx="4" fill="#f5962c" stroke="none"/>
        <rect x="14" y="48" width="28" height="28" rx="4" fill="#f5962c" stroke="none"/>
        <rect x="48" y="48" width="28" height="28" rx="4" fill="#f5962c" stroke="none"/>
        <g stroke="#fff" stroke-width="3">
          <path d="M28 20v16M20 28h16M54 28h16M22 54l12 12M34 54 22 66M54 62h16"/>
        </g>
        <g fill="#fff" stroke="none"><circle cx="62" cy="56" r="2"/><circle cx="62" cy="68" r="2"/></g>
      </svg>
      <h3>Audit, Accounting<br>and Tax</h3>
      <p>Lorem ipsum dolor sit amet, consectetur adipiscing elit, sed do eiusmod</p>
    </div>
    <div class="service">
      <svg width="110" height="90" viewBox="0 0 110 90">
        <path d="M30 22c-18 10-26 28-24 42 2 14 14 22 32 22h10c-6-6-8-14-8-22 0-14 8-26 20-32-4-4-10-8-16-10z" fill="#f5962c"/>
        <path d="M24 6h28l-6 12H30z" fill="#f5962c"/>
        <text x="20" y="66" font-family="Roboto,sans-serif" font-weight="700" font-size="30" fill="#fff">$</text>
        <circle cx="76" cy="62" r="24" fill="none" stroke="#f5962c" stroke-width="6"/>
        <path d="M76 48v14l9 8" fill="none" stroke="#f5962c" stroke-width="5"/>
      </svg>
      <h3>Financial<br>Management</h3>
      <p>Lorem ipsum dolor sit amet, consectetur adipiscing elit, sed do eiusmod</p>
    </div>
    <div class="service">
      <svg width="110" height="90" viewBox="0 0 110 90" fill="none" stroke="#f5962c" stroke-width="4">
        <circle cx="22" cy="48" r="10"/><circle cx="22" cy="48" r="17" stroke-dasharray="6 5" stroke-width="7"/>
        <circle cx="44" cy="20" r="7"/><circle cx="44" cy="20" r="12" stroke-dasharray="5 4" stroke-width="6"/>
        <rect x="44" y="34" width="52" height="36" rx="2"/>
        <path d="M36 78h68l-6-8H42z" fill="#f5962c"/>
      </svg>
      <h3>Information<br>Technology</h3>
      <p>Lorem ipsum dolor sit amet, consectetur adipiscing elit, sed do eiusmod</p>
    </div>
    <div class="service">
      <svg width="90" height="90" viewBox="0 0 90 90" fill="none" stroke="#f5962c" stroke-width="5">
        <path d="M45 4 10 16v26c0 22 15 36 35 44 20-8 35-22 35-44V16z"/>
        <path d="M45 14 20 23v19c0 16 11 27 25 33 14-6 25-17 25-33V23z" stroke-width="3"/>
        <path d="M30 44l12 12 26-28" stroke-width="7"/>
      </svg>
      <h3>Governance, Risk and<br>Compliance</h3>
      <p>Lorem ipsum dolor sit amet, consectetur adipiscing elit, sed do eiusmod</p>
    </div>
  </div>
</section>

<section class="industries">
  <h2 class="section-title">INDUSTRIES</h2>
  <div class="title-rule"></div>
  <p class="industries-intro">We specialize in the industries below offering customized services in assurance, financial management, technology, and risk and compliance services to support your business objectives and strategies.</p>
  <div class="industry-list">
    <div class="industry"><div class="industry-photo photo-capitol" role="img" aria-label="Photo of a domed government capitol building under a blue sky"></div><h3>Federal Government</h3></div>
    <div class="industry"><div class="industry-photo photo-columns" role="img" aria-label="Photo looking up at classical stone columns"></div><h3>State and Local Government</h3></div>
    <div class="industry"><div class="industry-photo photo-finance" role="img" aria-label="Illustration of a hand drawing financial services icons on a sky background"></div><h3>Financial Services</h3></div>
    <div class="industry"><div class="industry-photo photo-nonprofit" role="img" aria-label="Photo of a hand writing the words non profit with a red circle"></div><h3>Not-For-Profit</h3></div>
  </div>
</section>

<section class="partners">
  <div class="badge-list">
    <div class="badge"><span></span></div>
    <div class="badge"><span></span></div>
    <div class="badge"><span></span></div>
    <div class="badge"><span></span></div>
    <div class="badge"><span></span></div>
    <div class="badge"><span></span></div>
  </div>
</section>

<footer class="site-footer">
  <div class="footer-cols">
    <div class="footer-col">
      <h4>Services and Solution</h4>
      <ul><li>Audit, Accounting and Tax</li><li>Financial Management</li><li>Information Technology</li><li>Governance, Risk and Compliance</li></ul>
    </div>
    <div class="footer-col">
      <h4>Industries</h4>
      <ul><li>Federal Government</li><li>State and Local Government</li><li>Financial Services</li><li>Not-for-Profit</li></ul>
    </div>
    <div class="footer-col">
      <h4>About Us</h4>
      <ul><li>Company Overview</li><li>Management</li><li>Clients</li><li>Careers</li></ul>
    </div>
    <div class="footer-col contact">
      <h4>Contact Info</h4>
      <ul>
        <li><svg width="12" height="14" viewBox="0 0 12 14"><path d="M6 0a5 5 0 0 0-5 5c0 4 5 9 5 9s5-5 5-9a5 5 0 0 0-5-5z" fill="#f5962c"/><circle cx="6" cy="5" r="2" fill="#1a1a1a"/></svg>418 Larkwood Avenue NW, Suite 210<br>Carrow City, ST 20417</li>
        <li><svg width="12" height="14" viewBox="0 0 12 14"><rect x="3" y="0" width="6" height="14" rx="1.5" fill="#f5962c"/></svg>Phone: (555) 310-4826</li>
        <li><svg width="12" height="14" viewBox="0 0 12 14"><rect x="0" y="4" width="12" height="8" rx="1" fill="#f5962c"/><rect x="3" y="0" width="6" height="5" fill="#f5962c"/></svg>Fax: (555) 310-4827</li>
        <li><svg width="12" height="14" viewBox="0 0 12 14"><rect x="0" y="3" width="12" height="9" fill="#f5962c"/><path d="M0 3l6 5 6-5" fill="none" stroke="#1a1a1a" stroke-width="1.2"/></svg>Email: info@kelvorant.com</li>
      </ul>
    </div>
  </div>
  <div class="footer-bottom">
    Privacy Policy | Cookie Policy | Conditions of Use | Notice and Take Down Policy | Powered by Novaro<br>
    © 2016. The content on this website is owned by us and our licensors. Do not copy any content (including images) without our consent.
  </div>
</footer>

</body>
</html>
```